3 out of 100 people will get deadly skin cancer - we need a great illustration that shows this!

We put together a prototype image that communicates lifetime skin cancer risk. (see attached). We are looking for illustrators who can take make a new/better/cooler graphic that communicates this idea. It could be as simple as a superior illustration of the graphic we have or illustrators can propose a completely different idea.What should the illustration communicate?U.S. adults have a lifetime risk of developing skin cancer of 1 in 5. But we don't want to show 1 in 5; we want to show that number in a larger group. For example, in the attached illustration we show 20 in 100 people get skin cancer (i.e., 100 beach towels/umbrellas and 20 of them are red). Research has shown that people are more likely to accurately understand numbers like this when you convey them for larger groups (i.e., 20 out of 100 rather than 1 out of 5). U.S. adults also have a lifetime risk of 2.3% of developing the deadliest form of skin cancer (melanoma). In other words, approximately 3 in 100 people will develop melanoma in their lifetime. Ideally, a single image will convey both lifetime skin cancer risk (20 in 100) and melanoma risk (3 in 100). We will award a top three as follows: 1st place = $300, 2nd place = $250, third place = $200. We will also buy any design beyond 3rd place that we like for $100. For example, we purchased 24 designs in our last contest on Artmarketly.This research is supported by funding from the Corvane Institute of Science.

Target Market(s)

The U.S. public; individuals at high risk of developing skin cancer

Industry/Entity Type

Medicine

Colors

Designer to choose colors to be used in the design.

Requirements
Must have
• an original illustration that conveys both lifetime risk of developing skin cancer (20 in 100) and melanoma (3 in 100).
Nice to have
• It can be beach towels and umbrellas, just like our prototype, or the designers can pitch an original idea. Imagery can be realistic or cartoonish (or something in between). It should be illustrations, though. Not edited photos. The image should be in color (no black and white illustrations).
Should not have
• Photos. Clip art. Free vector images.
• We are looking for original illustrations created by the designer.

```html
<!DOCTYPE html>
<html lang="en">
<head>
<meta charset="utf-8">
<title>How Likely Are You to Get Skin Cancer?</title>
<link rel="stylesheet" href="https://fonts.googleapis.com/css2?family=Roboto+Condensed:wght@500&family=Open+Sans:wght@800&display=swap">
<style>
  :root {
    --page: #ffffff;
    --banner-red: #ee2a2b;
    --ink: #1a1a1a;
    --risk-none: #2f3990;
    --risk-skin: #e8232a;
    --risk-melanoma: #111111;
    --sun-core: #f8c93a;
    --sun-ray: #f0b13a;
    --sky: #7fb8e0;
    --sand-light: #f6cf4a;
    --sand-deep: #c27d38;
  }
  html, body {
    margin: 0;
    width: 1200px;
    height: 1200px;
    overflow: hidden;
    background: var(--page);
  }
  .poster {
    position: absolute;
    left: 188px;
    top: 6px;
    width: 824px;
    height: 1188px;
    display: block;
  }
  .headline {
    font-family: "Roboto Condensed", "Arial Narrow", sans-serif;
    font-weight: 500;
    font-size: 24px;
    fill: var(--ink);
  }
  .headline-title { text-decoration: underline; }
  .legend-label {
    font-family: "Open Sans", Arial, sans-serif;
    font-weight: 800;
    font-size: 20px;
    fill: var(--ink);
  }
  .no-cancer { fill: var(--risk-none); }
  .skin-cancer { fill: var(--risk-skin); }
  .melanoma { fill: var(--risk-melanoma); }
</style>
</head>
<body>
<svg class="poster" viewBox="157 5 686 990" xmlns="http://www.w3.org/2000/svg">
  <defs>
    <radialGradient id="sunburst-fill" cx="0.66" cy="0.58" r="0.8">
      <stop offset="0" stop-color="var(--sun-core)"/>
      <stop offset="0.25" stop-color="#f7c640"/>
      <stop offset="0.6" stop-color="var(--sun-ray)"/>
      <stop offset="1" stop-color="#f3c56a"/>
    </radialGradient>
    <linearGradient id="beach-fill" x1="0" y1="0" x2="0" y2="1">
      <stop offset="0" stop-color="var(--sky)"/>
      <stop offset="0.1" stop-color="#c8d49a"/>
      <stop offset="0.2" stop-color="var(--sand-light)"/>
      <stop offset="0.55" stop-color="#e4a93f"/>
      <stop offset="1" stop-color="var(--sand-deep)"/>
    </linearGradient>
    <linearGradient id="banner-fill" x1="0" y1="0" x2="1" y2="0">
      <stop offset="0" stop-color="var(--banner-red)"/>
      <stop offset="0.3" stop-color="var(--banner-red)"/>
      <stop offset="0.6" stop-color="#f07a2c" stop-opacity="0.85"/>
      <stop offset="1" stop-color="#f5b55a" stop-opacity="0"/>
    </linearGradient>
    <symbol id="person" viewBox="0 0 18 44" width="18" height="44">
      <circle cx="9" cy="5" r="4.5"/>
      <rect x="2.5" y="10.5" width="13" height="16" rx="3"/>
      <rect x="4" y="23" width="4.4" height="21" rx="2"/>
      <rect x="9.6" y="23" width="4.4" height="21" rx="2"/>
    </symbol>
  </defs>

  <rect class="sunburst" x="157" y="5" width="686" height="456" fill="url(#sunburst-fill)" role="img" aria-label="Illustration of a large bright sun with radiating rays"/>

  <g class="question-banner">
    <rect x="157" y="30" width="686" height="193" fill="url(#banner-fill)"/>
    <text class="headline headline-title" x="178" y="68">HOW LIKELY ARE YOU TO GET SKIN CANCER ?</text>
    <text class="headline" x="178" y="99">LET’S SAY 100 PEOPLE GO TO THE BEACH . . .</text>
    <text class="headline" x="178" y="143">HOW MANY WILL DEVELOP SKIN CANCER IN THEIR</text>
    <text class="headline" x="178" y="172">LIFETIME? HOW MANY WILL DEVELOP MELANOMA,</text>
    <text class="headline" x="178" y="202">THE DEADLIEST FORM OF SKIN CANCER ?</text>
  </g>

  <g class="legend">
    <use href="#person" class="skin-cancer" x="183" y="302"/>
    <text class="legend-label" x="207" y="331">= skin cancer</text>
    <use href="#person" class="melanoma" x="425" y="302"/>
    <text class="legend-label" x="449" y="331">= melanoma</text>
    <use href="#person" class="no-cancer" x="641" y="302"/>
    <text class="legend-label" x="665" y="331">= no skin cancer</text>
  </g>

  <rect class="beach" x="157" y="461" width="686" height="534" fill="url(#beach-fill)" role="img" aria-label="Illustration of sunlit sand dunes under a blue sky"/>

  <g class="risk-chart" aria-label="100 people: 20 get skin cancer, 3 of them melanoma">
    <g class="back-row">
      <use href="#person" class="no-cancer" x="290" y="486"/>
      <use href="#person" class="no-cancer" x="372" y="486"/>
      <use href="#person" class="melanoma" x="449" y="486"/>
      <use href="#person" class="no-cancer" x="535" y="486"/>
    </g>
    <g class="second-row">
      <use href="#person" class="no-cancer" x="182" y="533"/>
      <use href="#person" class="skin-cancer" x="239" y="533"/>
      <use href="#person" class="no-cancer" x="296" y="533"/>
      <use href="#person" class="no-cancer" x="353" y="533"/>
      <use href="#person" class="no-cancer" x="410" y="533"/>
      <use href="#person" class="no-cancer" x="467" y="533"/>
      <use href="#person" class="no-cancer" x="524" y="533"/>
      <use href="#person" class="no-cancer" x="581" y="533"/>
      <use href="#person" class="skin-cancer" x="637" y="533"/>
      <use href="#person" class="no-cancer" x="694" y="533"/>
      <use href="#person" class="skin-cancer" x="749" y="541"/>
      <use href="#person" class="no-cancer" x="804" y="553"/>
    </g>
    <g class="grid-row">
      <use href="#person" class="no-cancer" x="176" y="593"/><use href="#person" class="no-cancer" x="233" y="593"/><use href="#person" class="no-cancer" x="290" y="593"/><use href="#person" class="skin-cancer" x="347" y="593"/><use href="#person" class="no-cancer" x="404" y="593"/><use href="#person" class="no-cancer" x="461" y="593"/><use href="#person" class="no-cancer" x="518" y="593"/><use href="#person" class="no-cancer" x="575" y="593"/><use href="#person" class="no-cancer" x="632" y="593"/><use href="#person" class="skin-cancer" x="689" y="593"/>
    </g>
    <g class="grid-row">
      <use href="#person" class="no-cancer" x="176" y="646"/><use href="#person" class="skin-cancer" x="233" y="646"/><use href="#person" class="no-cancer" x="290" y="646"/><use href="#person" class="no-cancer" x="347" y="646"/><use href="#person" class="no-cancer" x="404" y="646"/><use href="#person" class="no-cancer" x="461" y="646"/><use href="#person" class="no-cancer" x="518" y="646"/><use href="#person" class="skin-cancer" x="575" y="646"/><use href="#person" class="no-cancer" x="632" y="646"/><use href="#person" class="no-cancer" x="689" y="646"/>
    </g>
    <g class="grid-row">
      <use href="#person" class="no-cancer" x="176" y="700"/><use href="#person" class="no-cancer" x="233" y="700"/><use href="#person" class="no-cancer" x="290" y="700"/><use href="#person" class="no-cancer" x="347" y="700"/><use href="#person" class="no-cancer" x="404" y="700"/><use href="#person" class="no-cancer" x="461" y="700"/><use href="#person" class="skin-cancer" x="518" y="700"/><use href="#person" class="no-cancer" x="575" y="700"/><use href="#person" class="no-cancer" x="632" y="700"/><use href="#person" class="no-cancer" x="689" y="700"/>
    </g>
    <g class="grid-row">
      <use href="#person" class="no-cancer" x="176" y="753"/><use href="#person" class="no-cancer" x="233" y="753"/><use href="#person" class="no-cancer" x="290" y="753"/><use href="#person" class="no-cancer" x="347" y="753"/><use href="#person" class="no-cancer" x="404" y="753"/><use href="#person" class="no-cancer" x="461" y="753"/><use href="#person" class="skin-cancer" x="518" y="753"/><use href="#person" class="no-cancer" x="575" y="753"/><use href="#person" class="no-cancer" x="632" y="753"/><use href="#person" class="no-cancer" x="689" y="753"/>
    </g>
    <g class="grid-row">
      <use href="#person" class="no-cancer" x="176" y="808"/><use href="#person" class="no-cancer" x="233" y="808"/><use href="#person" class="no-cancer" x="290" y="808"/><use href="#person" class="no-cancer" x="347" y="808"/><use href="#person" class="skin-cancer" x="404" y="808"/><use href="#person" class="no-cancer" x="461" y="808"/><use href="#person" class="no-cancer" x="518" y="808"/><use href="#person" class="no-cancer" x="575" y="808"/><use href="#person" class="skin-cancer" x="632" y="808"/><use href="#person" class="no-cancer" x="689" y="808"/>
    </g>
    <g class="grid-row">
      <use href="#person" class="no-cancer" x="176" y="862"/><use href="#person" class="no-cancer" x="233" y="862"/><use href="#person" class="skin-cancer" x="290" y="862"/><use href="#person" class="melanoma" x="347" y="862"/><use href="#person" class="no-cancer" x="404" y="862"/><use href="#person" class="no-cancer" x="461" y="862"/><use href="#person" class="no-cancer" x="518" y="862"/><use href="#person" class="no-cancer" x="575" y="862"/><use href="#person" class="no-cancer" x="632" y="862"/><use href="#person" class="no-cancer" x="689" y="862"/>
    </g>
    <g class="grid-row">
      <use href="#person" class="no-cancer" x="176" y="916"/><use href="#person" class="no-cancer" x="233" y="916"/><use href="#person" class="skin-cancer" x="290" y="916"/><use href="#person" class="no-cancer" x="347" y="916"/><use href="#person" class="no-cancer" x="404" y="916"/><use href="#person" class="skin-cancer" x="461" y="916"/><use href="#person" class="no-cancer" x="518" y="916"/><use href="#person" class="no-cancer" x="575" y="916"/><use href="#person" class="no-cancer" x="632" y="916"/><use href="#person" class="no-cancer" x="689" y="916"/>
    </g>
    <g class="grid-column">
      <use href="#person" class="skin-cancer" x="743" y="598"/><use href="#person" class="no-cancer" x="743" y="655"/><use href="#person" class="no-cancer" x="743" y="708"/><use href="#person" class="no-cancer" x="743" y="762"/><use href="#person" class="skin-cancer" x="743" y="816"/><use href="#person" class="no-cancer" x="743" y="871"/><use href="#person" class="no-cancer" x="743" y="923"/>
    </g>
    <g class="grid-column">
      <use href="#person" class="no-cancer" x="799" y="613"/><use href="#person" class="no-cancer" x="799" y="667"/><use href="#person" class="skin-cancer" x="799" y="720"/><use href="#person" class="no-cancer" x="799" y="775"/><use href="#person" class="no-cancer" x="799" y="829"/><use href="#person" class="no-cancer" x="799" y="883"/><use href="#person" class="melanoma" x="799" y="936"/>
    </g>
  </g>
</svg>
</body>
</html>
```